Real Estate Investment Company

Design Powerpoint slides are consistent with our logo, colors, and typeface. These Powerpoint slides will be used in all aspects of the business from live presentations to presentation decks available on a website or via email. Need to have different slide types created that allow for different types of slides such as cover pages, text heavy pages, image and chart heavy pages, multiple column pages, and mixed content pages.

Reason: to give additional time to get the design correct. I plan on making a selection in the next day or 2

Target Market(s)

Real Estate Investors

Industry/Entity Type

Investment

Other font styles liked:
• Consistent with logo

Requirements
Must have
• Our colors
• Our logo where possible
• Different slide designs of the same theme to allow for different types of slides such as cover pages, text heavy, picture heavy, and mixed content.
• Slides in both portrait and landscape orientation
Nice to have

```html
<!DOCTYPE html>
<html lang="en">
<head>
<meta charset="utf-8">
<title>Halvorne Management – Presentation Slide Set</title>
<link href="https://fonts.googleapis.com/css2?family=Libre+Baskerville:wght@400;700&family=Roboto:wght@400;500;700&display=swap" rel="stylesheet">
<style>
:root{
  --navy:#2f3c8e;
  --navy-dark:#26306f;
  --navy-soft:#4a58ad;
  --blue:#2d4aa6;
  --sky:#b9c0e2;
  --ink:#2b3566;
  --grey:#8b90a4;
  --rule:#d9dcea;
  --page:#e8e9ee;
  --white:#ffffff;
  --accent:#e0894a;
}
*{box-sizing:border-box;margin:0;padding:0}
html,body{width:1058px;height:1200px;overflow:hidden;background:var(--page)}
body{font-family:"Roboto",Arial,sans-serif;color:var(--ink)}
.deck{display:grid;grid-template-columns:repeat(3,346px);grid-template-rows:repeat(6,194px);gap:5px;padding:5px}
.slide{position:relative;background:var(--white);overflow:hidden}
.abs{position:absolute}
.slide-title{position:absolute;left:15px;top:11px;font:700 10.5px "Libre Baskerville",Georgia,serif;color:var(--ink);padding-bottom:3px;border-bottom:1.2px solid var(--navy)}
.brand{position:absolute;top:9px;right:8px;width:40px;text-align:center;font:700 3.6px/1.2 "Libre Baskerville",Georgia,serif;color:var(--navy);letter-spacing:.2px}
.brand-lg{font:700 7.5px/1.3 "Libre Baskerville",Georgia,serif;color:var(--white);letter-spacing:.8px;text-align:center}
.brand-lg .sq{display:block;width:14px;height:14px;background:var(--white);margin:0 auto 4px}
.skyline{position:absolute;left:0;right:0;bottom:3px;height:16px;background:linear-gradient(to top,#aab3dc,rgba(185,192,226,.15))}
.baseline{position:absolute;left:0;right:0;bottom:0;height:3px;background:var(--navy)}
.foot{position:absolute;left:6px;bottom:5px;font:400 3px "Roboto",sans-serif;color:var(--navy)}
.pg{position:absolute;right:6px;bottom:3px;width:10px;height:8px;background:var(--navy);color:#fff;font:500 3.4px/8px "Roboto",sans-serif;text-align:center}
.lead{font:700 8px/1.3 "Roboto",sans-serif;color:var(--blue)}
.sub{font:400 6.4px "Libre Baskerville",Georgia,serif;color:var(--blue)}
.copy{font:400 4.2px/1.45 "Roboto",sans-serif;color:var(--grey)}
.copy + .copy{margin-top:4px}
.copy.light{color:#d7dbf0}
.photo{position:absolute}
.ic{display:inline-flex;align-items:center;justify-content:center;width:12px;height:12px;border-radius:50%;background:var(--navy);flex:none}
.ic svg{width:8px;height:8px}
.ic.lg{width:17px;height:17px}
.ic.lg svg{width:10px;height:10px}
.ic.ring{background:transparent;border:1px solid #fff}
.ic.pale{background:#8d99d6}
.bullet{position:absolute;display:flex;gap:5px;width:80px}
.bullet h4{font:700 5.2px "Roboto",sans-serif;color:var(--blue);margin:1px 0 1px}
.bullet .copy{font-size:3.6px}
.col-item{position:absolute;width:58px;text-align:center}
.col-item .ic{margin:0 auto 4px}
.col-item h4{font:700 5.2px "Roboto",sans-serif;color:var(--blue);margin-bottom:2px}
.col-item .copy{font-size:3.6px}
</style>
</head>
<body>
<svg width="0" height="0" style="position:absolute" aria-hidden="true">
  <defs>
    <symbol id="i-search" viewBox="0 0 16 16"><circle cx="7" cy="7" r="4" fill="none" stroke="#fff" stroke-width="2"/><line x1="10" y1="10" x2="13.5" y2="13.5" stroke="#fff" stroke-width="2.2" stroke-linecap="round"/></symbol>
    <symbol id="i-pen" viewBox="0 0 16 16"><path d="M3.5 12.5 L4.3 9.6 L10.8 3.1 L12.9 5.2 L6.4 11.7 Z" fill="#fff"/></symbol>
    <symbol id="i-heart" viewBox="0 0 16 16"><path d="M8 13.5C2 9.3 2.6 3.8 5.8 4.1 7 4.2 8 5.6 8 5.6S9 4.2 10.2 4.1C13.4 3.8 14 9.3 8 13.5Z" fill="#fff"/></symbol>
    <symbol id="i-gear" viewBox="0 0 16 16"><circle cx="8" cy="8" r="2.6" fill="none" stroke="#fff" stroke-width="1.8"/><circle cx="8" cy="8" r="5.2" fill="none" stroke="#fff" stroke-width="2.2" stroke-dasharray="2 1.6"/></symbol>
    <symbol id="i-tick" viewBox="0 0 16 16"><polyline points="3.5,8.5 6.8,11.5 12.5,4.5" fill="none" stroke="#fff" stroke-width="2.2" stroke-linecap="round" stroke-linejoin="round"/></symbol>
    <symbol id="i-clip" viewBox="0 0 16 16"><path d="M10.5 5 L6 9.5 a1.3 1.3 0 0 0 1.8 1.8 L12 7 a2.8 2.8 0 0 0 -4 -4 L3.8 7.3 a4 4 0 0 0 5.6 5.6 L12 10.3" fill="none" stroke="#fff" stroke-width="1.3" stroke-linecap="round"/></symbol>
    <symbol id="i-people" viewBox="0 0 16 16"><circle cx="8" cy="5.5" r="2" fill="#fff"/><circle cx="4" cy="6.5" r="1.5" fill="#fff"/><circle cx="12" cy="6.5" r="1.5" fill="#fff"/><path d="M4.5 12.5c0-2.5 1.5-4 3.5-4s3.5 1.5 3.5 4Z" fill="#fff"/><path d="M1.5 12.5c0-2 1-3.3 2.5-3.3 1 0 1.5.4 1.5.4-.7.9-1 1.8-1 2.9Z" fill="#fff"/><path d="M14.5 12.5c0-2-1-3.3-2.5-3.3-1 0-1.5.4-1.5.4.7.9 1 1.8 1 2.9Z" fill="#fff"/></symbol>
    <symbol id="i-bars" viewBox="0 0 16 16"><rect x="3" y="9" width="2" height="4" fill="#fff"/><rect x="7" y="6" width="2" height="7" fill="#fff"/><rect x="11" y="3" width="2" height="10" fill="#fff"/></symbol>
    <symbol id="i-star" viewBox="0 0 16 16"><path d="M8 2.5 9.6 6.2 13.5 6.5 10.5 9 11.5 13 8 10.8 4.5 13 5.5 9 2.5 6.5 6.4 6.2Z" fill="#fff"/></symbol>
    <symbol id="i-home" viewBox="0 0 16 16"><path d="M2 8 8 2.8 14 8H12V13.5H4V8Z" fill="#fff"/></symbol>
    <symbol id="i-phone" viewBox="0 0 16 16"><path d="M4.5 2.5 6.8 5 5.6 6.6C6.4 8.4 7.6 9.6 9.4 10.4L11 9.2 13.5 11.5 12 13.5C7 13 3 9 2.5 4Z" fill="#fff"/></symbol>
    <symbol id="i-mail" viewBox="0 0 16 16"><rect x="2" y="4" width="12" height="8.5" fill="#fff"/><polyline points="2,4 8,9 14,4" fill="none" stroke="#2f3c8e" stroke-width="1.2"/></symbol>
    <symbol id="i-globe" viewBox="0 0 16 16"><circle cx="8" cy="8" r="5.5" fill="none" stroke="#fff" stroke-width="1.4"/><ellipse cx="8" cy="8" rx="2.3" ry="5.5" fill="none" stroke="#fff" stroke-width="1.1"/><line x1="2.5" y1="8" x2="13.5" y2="8" stroke="#fff" stroke-width="1.1"/></symbol>
    <symbol id="i-cup" viewBox="0 0 16 16"><path d="M3 7H11V10.5A3 3 0 0 1 8 13.5H6A3 3 0 0 1 3 10.5Z" fill="#fff"/><path d="M11 8H12.3A1.5 1.5 0 0 1 12.3 11H10.8" fill="none" stroke="#fff" stroke-width="1.1"/><path d="M6 2.5C5 3.8 7 4.4 6 5.8M8.5 2.5C7.5 3.8 9.5 4.4 8.5 5.8" fill="none" stroke="#fff" stroke-width="0.9"/><rect x="2" y="14" width="11" height="1" fill="#fff"/></symbol>
  </defs>
</svg>

<main class="deck">

  <!-- Quote -->
  <section class="slide slide-quote">
    <h2 class="slide-title">Quote Area</h2>
    <div class="brand">HALVORNE<br>MANAGEMENT</div>
    <div class="abs" style="left:6px;top:46px;width:172px;height:121px;background:var(--navy)">
      <p class="abs" style="left:24px;top:36px;width:140px;font:400 7.6px/1.35 'Roboto',sans-serif;color:#fff">“ Coming together is a beginning.<br>Keeping together is progress.<br>Working together is success. ”</p>
      <p class="abs" style="left:28px;top:82px;font:400 5px 'Roboto',sans-serif;color:#fff">- Corwin Ashdale -</p>
    </div>
    <div class="photo" role="img" aria-label="Photo of a furnished living room with a sofa and lamp" style="left:178px;top:46px;width:168px;height:121px;background:linear-gradient(135deg,#c9b9a3,#8e8173 55%,#5d5248)"></div>
    <div class="skyline" role="img" aria-label="City skyline silhouette"></div><div class="baseline"></div>
    <span class="foot">halvorne management</span><span class="pg">22</span>
  </section>

  <!-- Two Column -->
  <section class="slide slide-two-col">
    <h2 class="slide-title">Two Column Description</h2>
    <div class="brand">HALVORNE<br>MANAGEMENT</div>
    <p class="lead abs" style="left:16px;top:50px">We are Halvorne Management<br>Ready to Help You to Get an Incredible Apartment</p>
    <div class="abs" style="left:16px;top:88px;width:150px">
      <p class="copy">Clear plans for every property we manage, built on steady returns and careful upkeep.</p>
      <p class="copy">Tenants and owners get quick answers, honest reports and homes kept in good order.</p>
    </div>
    <div class="abs" style="left:173px;top:88px;width:1px;height:82px;background:var(--rule)"></div>
    <div class="abs" style="left:188px;top:88px;width:150px">
      <p class="copy">Clear plans for every property we manage, built on steady returns and careful upkeep.</p>
      <p class="copy">Tenants and owners get quick answers, honest reports and homes kept in good order.</p>
    </div>
    <div class="skyline" role="img" aria-label="City skyline silhouette"></div><div class="baseline"></div>
    <span class="foot">halvorne management</span><span class="pg">23</span>
  </section>

  <!-- Pictures with Bullets -->
  <section class="slide slide-pictures">
    <h2 class="slide-title">Pictures with Bullets</h2>
    <div class="brand">HALVORNE<br>MANAGEMENT</div>
    <div class="photo" role="img" aria-label="Strip of three property photos: house exterior, interior room and kitchen" style="left:48px;top:50px;width:250px;height:39px;background:linear-gradient(90deg,#7d9a6a,#a7a79b 35%,#c2b8a8 65%,#8b7c6c)"></div>
    <span class="ic abs" style="left:88px;top:64px"><svg><use href="#i-search"/></svg></span>
    <span class="ic abs" style="left:148px;top:64px"><svg><use href="#i-gear"/></svg></span>
    <span class="ic abs" style="left:227px;top:64px"><svg><use href="#i-people"/></svg></span>
    <div class="abs" style="left:48px;top:108px;width:118px">
      <h3 class="sub">Your Title Goes Here</h3>
      <p class="copy" style="margin-top:2px">Clear plans for every property we manage, built on steady returns and careful upkeep.</p>
      <p class="copy">Short note on this point.</p>
    </div>
    <div class="abs" style="left:183px;top:108px;width:118px">
      <h3 class="sub">Your Title Goes Here</h3>
      <p class="copy" style="margin-top:2px">Clear plans for every property we manage, built on steady returns and careful upkeep.</p>
      <p class="copy">Short note on this point.</p>
    </div>
    <div class="skyline" role="img" aria-label="City skyline silhouette"></div><div class="baseline"></div>
    <span class="foot">halvorne management</span><span class="pg">24</span>
  </section>

  <!-- Team cover -->
  <section class="slide slide-team-cover">
    <div class="photo" role="img" aria-label="Group photo of four team members standing outside an office in winter" style="left:0;top:0;width:206px;height:194px;background:linear-gradient(160deg,#9ea1a6,#6d6a67 50%,#3e3b3a)"></div>
    <div class="abs" style="left:206px;top:0;width:140px;height:194px;background:linear-gradient(180deg,rgba(47,60,142,.92),rgba(38,48,111,.96))">
      <div class="brand-lg abs" style="left:0;right:0;top:20px"><span class="sq"></span>HALVORNE MANAGEMENT</div>
      <div class="abs" style="left:14px;top:64px;display:flex;gap:18px">
        <span class="ic lg ring"><svg><use href="#i-tick"/></svg></span>
        <span class="ic lg ring"><svg><use href="#i-search"/></svg></span>
        <span class="ic lg ring"><svg><use href="#i-star"/></svg></span>
      </div>
      <h3 class="abs" style="left:14px;top:112px;font:400 6.4px 'Libre Baskerville',serif;color:#fff">Your Title Goes Here</h3>
      <p class="copy light abs" style="left:14px;top:124px;width:100px">Clear plans for every property we manage, built on steady returns and careful upkeep.</p>
      <div class="abs" style="left:0;right:0;bottom:0;height:17px;background:var(--navy-soft);text-align:center;font:500 4.6px/17px 'Roboto',sans-serif;color:#fff">www.halvornemgmt.com</div>
    </div>
  </section>

  <!-- Coffee break -->
  <section class="slide slide-break" role="img" aria-label="Break slide with a steaming coffee cup in dim blue light" style="background:radial-gradient(ellipse at 55% 85%,#3b4a9e,#2a3580 55%,#232c6c)">
    <div class="abs" style="left:96px;top:46px;width:22px;height:22px"><svg width="22" height="22"><use href="#i-cup"/></svg></div>
    <p class="abs" style="left:42px;top:68px;font:700 12.5px 'Roboto',sans-serif;color:#fff;letter-spacing:.3px">COFFEE BREAK</p>
    <p class="abs" style="left:80px;top:85px;font:400 5px 'Libre Baskerville',serif;color:#dfe3f5">Back in 15 minutes</p>
  </section>

  <!-- Navy band with photo -->
  <section class="slide slide-band">
    <div class="abs" style="left:0;top:0;width:346px;height:110px;background:var(--navy)"></div>
    <div class="brand-lg abs" style="left:30px;top:16px;width:110px"><span class="sq"></span>HALVORNE MANAGEMENT</div>
    <div class="photo" role="img" aria-label="Photo of the office team gathered indoors" style="left:28px;top:62px;width:118px;height:97px;background:linear-gradient(150deg,#b7aa98,#7c6e62 60%,#574b42)"></div>
    <h3 class="abs" style="left:182px;top:48px;font:400 6.2px 'Libre Baskerville',serif;color:#fff">Your Title Goes Here</h3>
    <p class="copy light abs" style="left:182px;top:62px;width:150px">Clear plans for every property we manage, built on steady returns and careful upkeep.</p>
    <div class="bullet" style="left:165px;top:123px;width:74px"><span class="ic"><svg><use href="#i-search"/></svg></span><div><h4>Your Text Here</h4><p class="copy">Short note about this service item.</p></div></div>
    <div class="bullet" style="left:243px;top:123px;width:74px"><span class="ic"><svg><use href="#i-heart"/></svg></span><div><h4>Your Text Here</h4><p class="copy">Short note about this service item.</p></div></div>
    <div class="bullet" style="left:165px;top:156px;width:74px"><span class="ic"><svg><use href="#i-gear"/></svg></span><div><h4>Your Text Here</h4><p class="copy">Short note about this service item.</p></div></div>
    <div class="bullet" style="left:243px;top:156px;width:74px"><span class="ic"><svg><use href="#i-tick"/></svg></span><div><h4>Your Text Here</h4><p class="copy">Short note about this service item.</p></div></div>
    <div class="baseline"></div>
    <span class="foot">halvorne management</span><span class="pg">27</span>
  </section>

  <!-- Bullet & Chart -->
  <section class="slide slide-chart">
    <h2 class="slide-title">Bullet &amp; Chart Area</h2>
    <div class="brand">HALVORNE<br>MANAGEMENT</div>
    <svg class="abs" style="left:14px;top:50px" width="150" height="120" viewBox="0 0 150 120" role="img" aria-label="Horizontal bar chart of three series across four categories">
      <g font-family="Roboto,sans-serif" font-size="4" fill="#6b7090">
        <text x="0" y="14">Category 4</text><text x="0" y="39">Category 3</text><text x="0" y="64">Category 2</text><text x="0" y="89">Category 1</text>
      </g>
      <g>
        <rect x="45" y="8" width="105" height="3.5" fill="#2a3380"/><rect x="45" y="12" width="52" height="3.5" fill="#a3a6b2"/><rect x="45" y="16" width="82" height="3.5" fill="#3449b0"/>
        <rect x="45" y="33" width="54" height="3.5" fill="#2a3380"/><rect x="45" y="37" width="22" height="3.5" fill="#a3a6b2"/><rect x="45" y="41" width="64" height="3.5" fill="#3449b0"/>
        <rect x="45" y="58" width="28" height="3.5" fill="#2a3380"/><rect x="45" y="62" width="80" height="3.5" fill="#a3a6b2"/><rect x="45" y="66" width="44" height="3.5" fill="#3449b0"/>
        <rect x="45" y="83" width="30" height="3.5" fill="#2a3380"/><rect x="45" y="87" width="22" height="3.5" fill="#a3a6b2"/><rect x="45" y="91" width="80" height="3.5" fill="#3449b0"/>
      </g>
      <g font-family="Roboto,sans-serif" font-size="3.4" fill="#6b7090">
        <rect x="58" y="108" width="2" height="2" fill="#2a3380"/><text x="61.5" y="110">Series 3</text>
        <rect x="78" y="108" width="2" height="2" fill="#a3a6b2"/><text x="81.5" y="110">Series 2</text>
        <rect x="98" y="108" width="2" height="2" fill="#3449b0"/><text x="101.5" y="110">Series 1</text>
      </g>
    </svg>
    <div class="bullet" style="left:192px;top:56px;width:110px"><span class="ic"><svg><use href="#i-search"/></svg></span><div><h4>Your Text Here</h4><p class="copy">Short note about this service item.</p></div></div>
    <div class="bullet" style="left:192px;top:85px;width:110px"><span class="ic"><svg><use href="#i-pen"/></svg></span><div><h4>Your Text Here</h4><p class="copy">Short note about this service item.</p></div></div>
    <div class="bullet" style="left:192px;top:113px;width:110px"><span class="ic"><svg><use href="#i-tick"/></svg></span><div><h4>Your Text Here</h4><p class="copy">Short note about this service item.</p></div></div>
    <div class="bullet" style="left:192px;top:141px;width:110px"><span class="ic"><svg><use href="#i-gear"/></svg></span><div><h4>Your Text Here</h4><p class="copy">Short note about this service item.</p></div></div>
    <div class="skyline" role="img" aria-label="City skyline silhouette"></div><div class="baseline"></div>
    <span class="foot">halvorne management</span><span class="pg">28</span>
  </section>

  <!-- Bathroom photos -->
  <section class="slide slide-gallery">
    <div class="abs" style="left:0;top:0;width:121px;height:103px;background:var(--navy)"></div>
    <div class="brand-lg abs" style="left:8px;top:34px;width:105px"><span class="sq"></span>HALVORNE MANAGEMENT</div>
    <div class="photo" role="img" aria-label="Photo of a bathroom vanity with a window" style="left:0;top:103px;width:121px;height:91px;background:linear-gradient(160deg,#d9c8a4,#9d8763 60%,#6a5940)"></div>
    <div class="photo" role="img" aria-label="Photo of a renovated bathroom with tub and toilet" style="left:121px;top:0;width:120px;height:194px;background:linear-gradient(170deg,#cbb58a,#a38859 45%,#5b4a35)"></div>
    <div class="brand" style="right:8px">HALVORNE<br>MANAGEMENT</div>
    <div class="abs" style="left:258px;top:44px;width:80px">
      <h3 class="sub">Your Title Goes Here</h3>
      <p class="copy" style="margin-top:5px">Clear plans for every property we manage, built on steady returns and careful upkeep.</p>
      <p class="copy">Tenants and owners get quick answers, honest reports and homes kept in good order.</p>
      <p class="copy">Short note on this point.</p>
    </div>
    <div class="baseline"></div><span class="pg">29</span>
  </section>

  <!-- Paragraph with three bullets -->
  <section class="slide slide-three">
    <h2 class="slide-title">Paragraph with Three Bullet</h2>
    <div class="brand">HALVORNE<br>MANAGEMENT</div>
    <p class="lead abs" style="left:16px;top:44px">We are Halvorne Management<br>Ready to Help You to Get an Incredible Apartment</p>
    <div class="abs" style="left:16px;top:78px;width:105px">
      <p class="copy">Clear plans for every property we manage, built on steady returns and careful upkeep.</p>
      <p class="copy">Tenants and owners get quick answers, honest reports and homes kept in good order.</p>
    </div>
    <div class="abs" style="left:126px;top:78px;width:1px;height:90px;background:var(--rule)"></div>
    <div class="col-item" style="left:141px;top:72px"><span class="ic lg"><svg><use href="#i-pen"/></svg></span><h4>Your Text Here</h4><p class="copy">Short note about this service item.</p><p class="copy">Short note on this point.</p></div>
    <div class="col-item" style="left:210px;top:72px"><span class="ic lg"><svg><use href="#i-gear"/></svg></span><h4>Your Text Here</h4><p class="copy">Short note about this service item.</p><p class="copy">Short note on this point.</p></div>
    <div class="col-item" style="left:279px;top:72px"><span class="ic lg"><svg><use href="#i-clip"/></svg></span><h4>Your Text Here</h4><p class="copy">Short note about this service item.</p><p class="copy">Short note on this point.</p></div>
    <div class="skyline" role="img" aria-label="City skyline silhouette"></div><div class="baseline"></div>
    <span class="foot">halvorne management</span><span class="pg">30</span>
  </section>

  <!-- Four bullets with paragraph -->
  <section class="slide slide-four">
    <h2 class="slide-title">Four Bullets with Paragraph</h2>
    <div class="brand">HALVORNE<br>MANAGEMENT</div>
    <div class="bullet" style="left:26px;top:63px;width:74px"><span class="ic"><svg><use href="#i-search"/></svg></span><div><h4>Your Text Here</h4><p class="copy">Short note about this service item.</p></div></div>
    <div class="bullet" style="left:103px;top:63px;width:74px"><span class="ic"><svg><use href="#i-heart"/></svg></span><div><h4>Your Text Here</h4><p class="copy">Short note about this service item.</p></div></div>
    <div class="bullet" style="left:26px;top:119px;width:74px"><span class="ic"><svg><use href="#i-gear"/></svg></span><div><h4>Your Text Here</h4><p class="copy">Short note about this service item.</p></div></div>
    <div class="bullet" style="left:103px;top:119px;width:74px"><span class="ic"><svg><use href="#i-tick"/></svg></span><div><h4>Your Text Here</h4><p class="copy">Short note about this service item.</p></div></div>
    <div class="abs" style="left:205px;top:63px;width:125px">
      <h3 class="sub">Your Title Goes Here</h3>
      <p class="copy" style="margin-top:5px">Clear plans for every property we manage, built on steady returns and careful upkeep.</p>
      <p class="copy">Tenants and owners get quick answers, honest reports and homes kept in good order.</p>
      <p class="copy">Short note on this point.</p>
    </div>
    <div class="skyline" role="img" aria-label="City skyline silhouette"></div><div class="baseline"></div>
    <span class="foot">halvorne management</span><span class="pg">31</span>
  </section>

  <!-- Our Differences -->
  <section class="slide slide-differences">
    <h2 class="slide-title">Our Differences</h2>
    <div class="brand">HALVORNE<br>MANAGEMENT</div>
    <div class="abs" style="left:18px;top:56px;width:310px;height:101px;background:var(--navy)">
      <div class="abs" style="left:14px;top:12px;width:165px;display:flex;flex-direction:column;gap:9px">
        <div style="display:flex;gap:6px;align-items:center"><span class="ic pale"><svg><use href="#i-tick"/></svg></span><p class="copy light" style="color:#fff">Every listing is checked, priced fairly and shown within a week.</p></div>
        <div style="display:flex;gap:6px;align-items:center"><span class="ic pale"><svg><use href="#i-gear"/></svg></span><p class="copy light" style="color:#fff">Owners see rent, repairs and vacancies in one monthly report.</p></div>
        <div style="display:flex;gap:6px;align-items:center"><span class="ic pale"><svg><use href="#i-pen"/></svg></span><p class="copy light" style="color:#fff">Every listing is checked, priced fairly and shown within a week.</p></div>
        <div style="display:flex;gap:6px;align-items:center"><span class="ic pale"><svg><use href="#i-search"/></svg></span><p class="copy light" style="color:#fff">Owners see rent, repairs and vacancies in one monthly report.</p></div>
      </div>
      <div class="photo" role="img" aria-label="Photo of a building entrance with a bicycle by the door" style="left:185px;top:12px;width:117px;height:78px;background:linear-gradient(150deg,#8a9a72,#5f6a4c 50%,#3f4636)"></div>
    </div>
    <div class="skyline" role="img" aria-label="City skyline silhouette"></div><div class="baseline"></div>
    <span class="foot">halvorne management</span><span class="pg">32</span>
  </section>

  <!-- Your Title -->
  <section class="slide slide-feature">
    <h2 class="slide-title">Your Title</h2>
    <div class="brand">HALVORNE<br>MANAGEMENT</div>
    <div class="abs" style="left:14px;top:57px;width:92px">
      <h3 class="sub">Your Title Goes Here</h3>
      <p class="copy" style="margin-top:5px">Clear plans for every property we manage, built on steady returns and careful upkeep.</p>
      <p class="copy">Tenants and owners get quick answers, honest reports and homes kept in good order.</p>
      <p class="copy">Short note on this point.</p>
    </div>
    <div class="photo" role="img" aria-label="Photo of a modern kitchen with wood cabinets and steel appliances" style="left:115px;top:0;width:121px;height:194px;background:linear-gradient(175deg,#c8b9a0,#7f6a52 45%,#4e3f30)"></div>
    <div class="bullet" style="left:246px;top:56px;width:92px"><span class="ic"><svg><use href="#i-search"/></svg></span><div><h4>Your Text Here</h4><p class="copy">Short note about this service item.</p></div></div>
    <div class="bullet" style="left:246px;top:84px;width:92px"><span class="ic"><svg><use href="#i-pen"/></svg></span><div><h4>Your Text Here</h4><p class="copy">Short note about this service item.</p></div></div>
    <div class="bullet" style="left:246px;top:112px;width:92px"><span class="ic"><svg><use href="#i-tick"/></svg></span><div><h4>Your Text Here</h4><p class="copy">Short note about this service item.</p></div></div>
    <div class="bullet" style="left:246px;top:140px;width:92px"><span class="ic"><svg><use href="#i-gear"/></svg></span><div><h4>Your Text Here</h4><p class="copy">Short note about this service item.</p></div></div>
    <div class="skyline" role="img" aria-label="City skyline silhouette" style="left:236px"></div><div class="baseline"></div>
    <span class="foot">halvorne management</span><span class="pg">33</span>
  </section>

  <!-- Text & Bullet -->
  <section class="slide slide-text-bullets">
    <h2 class="slide-title">Text &amp; Bullet Area</h2>
    <div class="brand">HALVORNE<br>MANAGEMENT</div>
    <div class="abs" style="left:16px;top:48px;width:92px">
      <h3 class="sub">Your Title Goes Here</h3>
      <p class="copy" style="margin-top:5px">Clear plans for every property we manage, built on steady returns and careful upkeep.</p>
      <p class="copy">Tenants and owners get quick answers, honest reports and homes kept in good order.</p>
      <p class="copy">Short note on this point.</p>
    </div>
    <div class="bullet" style="left:124px;top:48px;width:100px"><span class="ic"><svg><use href="#i-search"/></svg></span><div><h4>Your Text Here</h4><p class="copy">Short note about this service item.</p></div></div>
    <div class="bullet" style="left:124px;top:76px;width:100px"><span class="ic"><svg><use href="#i-pen"/></svg></span><div><h4>Your Text Here</h4><p class="copy">Short note about this service item.</p></div></div>
    <div class="bullet" style="left:124px;top:104px;width:100px"><span class="ic"><svg><use href="#i-tick"/></svg></span><div><h4>Your Text Here</h4><p class="copy">Short note about this service item.</p></div></div>
    <div class="bullet" style="left:124px;top:132px;width:100px"><span class="ic"><svg><use href="#i-gear"/></svg></span><div><h4>Your Text Here</h4><p class="copy">Short note about this service item.</p></div></div>
    <div class="bullet" style="left:236px;top:48px;width:100px"><span class="ic"><svg><use href="#i-search"/></svg></span><div><h4>Your Text Here</h4><p class="copy">Short note about this service item.</p></div></div>
    <div class="bullet" style="left:236px;top:76px;width:100px"><span class="ic"><svg><use href="#i-pen"/></svg></span><div><h4>Your Text Here</h4><p class="copy">Short note about this service item.</p></div></div>
    <div class="bullet" style="left:236px;top:104px;width:100px"><span class="ic"><svg><use href="#i-tick"/></svg></span><div><h4>Your Text Here</h4><p class="copy">Short note about this service item.</p></div></div>
    <div class="bullet" style="left:236px;top:132px;width:100px"><span class="ic"><svg><use href="#i-gear"/></svg></span><div><h4>Your Text Here</h4><p class="copy">Short note about this service item.</p></div></div>
    <div class="skyline" role="img" aria-label="City skyline silhouette"></div><div class="baseline"></div>
    <span class="foot">halvorne management</span><span class="pg">34</span>
  </section>

  <!-- Workflow -->
  <section class="slide slide-workflow">
    <h2 class="slide-title">Workflow Area</h2>
    <div class="brand">HALVORNE<br>MANAGEMENT</div>
    <p class="copy abs" style="left:26px;top:42px;width:296px;text-align:center">We follow a simple five step process from first call to signed lease, so investors always know what happens next and when it will be done.</p>
    <svg class="abs" style="left:0;top:60px" width="346" height="120" viewBox="0 0 346 120" aria-label="Five step workflow wave" role="img">
      <path d="M30 60 A29 29 0 0 1 88 60 A29 29 0 0 0 146 60 A29 29 0 0 1 204 60 A29 29 0 0 0 262 60 A29 29 0 0 1 320 60" fill="none" stroke="#2f3c8e" stroke-width="9"/>
      <g font-family="Roboto,sans-serif" font-size="4.5" font-weight="700" fill="#2b3566" text-anchor="middle">
        <circle cx="83" cy="45" r="5" fill="#fff" stroke="#2b3566" stroke-width=".6"/><text x="83" y="46.6">1</text>
        <circle cx="111" cy="79" r="5" fill="#fff" stroke="#2b3566" stroke-width=".6"/><text x="111" y="80.6">2</text>
        <circle cx="199" cy="45" r="5" fill="#fff" stroke="#2b3566" stroke-width=".6"/><text x="199" y="46.6">3</text>
        <circle cx="227" cy="79" r="5" fill="#fff" stroke="#2b3566" stroke-width=".6"/><text x="227" y="80.6">4</text>
        <circle cx="315" cy="45" r="5" fill="#fff" stroke="#2b3566" stroke-width=".6"/><text x="315" y="46.6">5</text>
        <text x="59" y="70" font-size="5.4">Data 1</text>
        <text x="117" y="19" font-size="5.4">Data 2</text>
        <text x="175" y="70" font-size="5.4">Data 3</text>
        <text x="233" y="19" font-size="5.4">Data 4</text>
        <text x="291" y="70" font-size="5.4">Data 5</text>
      </g>
      <g font-family="Roboto,sans-serif" font-size="4" fill="#8b90a4" text-anchor="middle">
        <text x="59" y="79">Short note</text><text x="59" y="84">about this step.</text>
        <text x="117" y="27">Short note</text><text x="117" y="32">about this step.</text>
        <text x="175" y="79">Short note</text><text x="175" y="84">about this step.</text>
        <text x="233" y="27">Short note</text><text x="233" y="32">about this step.</text>
        <text x="291" y="79">Short note</text><text x="291" y="84">about this step.</text>
      </g>
    </svg>
    <div class="skyline" role="img" aria-label="City skyline silhouette"></div><div class="baseline"></div>
    <span class="foot">halvorne management</span><span class="pg">35</span>
  </section>

  <!-- Key Points -->
  <section class="slide slide-keypoints">
    <h2 class="slide-title">Key Points Area</h2>
    <div class="brand">HALVORNE<br>MANAGEMENT</div>
    <p class="copy abs" style="left:26px;top:42px;width:296px;text-align:center">We follow a simple five step process from first call to signed lease, so investors always know what happens next and when it will be done.</p>
    <svg class="abs" style="left:0;top:65px" width="346" height="60" viewBox="0 0 346 60" role="img" aria-label="Five key measures shown as linked circles">
      <circle cx="95" cy="28" r="23" fill="#2f3c8e"/>
      <circle cx="136" cy="28" r="23" fill="#5262b6"/>
      <circle cx="177" cy="28" r="23" fill="#2f3c8e"/>
      <circle cx="218" cy="28" r="23" fill="#5262b6"/>
      <circle cx="259" cy="28" r="23" fill="#2f3c8e"/>
      <use href="#i-people" x="89" y="14" width="12" height="12"/>
      <use href="#i-tick" x="130" y="14" width="12" height="12"/>
      <use href="#i-bars" x="171" y="14" width="12" height="12"/>
      <use href="#i-heart" x="212" y="14" width="12" height="12"/>
      <use href="#i-star" x="253" y="14" width="12" height="12"/>
      <g font-family="Roboto,sans-serif" font-size="3.8" fill="#fff" text-anchor="middle">
        <text x="95" y="33">Visiting</text><text x="95" y="37.5">Customers</text>
        <text x="136" y="33">Closing</text><text x="136" y="37.5">Ratio</text>
        <text x="177" y="33">Profit</text><text x="177" y="37.5">per Sale</text>
        <text x="218" y="33">Customers</text><text x="218" y="37.5">Satisfaction</text>
        <text x="259" y="33">Branding</text><text x="259" y="37.5">Awareness</text>
      </g>
    </svg>
    <p class="copy abs" style="left:76px;top:132px;width:196px;text-align:center;color:#555a70">Each measure is tracked month by month and shared with owners so that decisions rest on clear numbers rather than guesswork or old habits.</p>
    <div class="skyline" role="img" aria-label="City skyline silhouette"></div><div class="baseline"></div>
    <span class="foot">halvorne management</span><span class="pg">36</span>
  </section>

  <!-- Table -->
  <section class="slide slide-table">
    <h2 class="slide-title">Table Area</h2>
    <div class="brand">HALVORNE<br>MANAGEMENT</div>
    <svg class="abs" style="left:56px;top:44px" width="242" height="120" viewBox="0 0 242 120" role="img" aria-label="Comparison table with two columns">
      <rect x="0" y="0" width="242" height="120" fill="#fff" stroke="#e1e3ee"/>
      <rect x="0" y="0" width="97" height="30" fill="#262f6f"/>
      <rect x="97" y="0" width="72" height="30" fill="#2f3c8e"/>
      <rect x="169" y="0" width="73" height="30" fill="#262f6f"/>
      <g font-family="Roboto,sans-serif" font-weight="700" font-size="6" fill="#fff">
        <text x="8" y="17">Description</text>
        <text x="133" y="13" text-anchor="middle">Column 1</text>
        <text x="205" y="13" text-anchor="middle">Column 2</text>
      </g>
      <circle cx="133" cy="29" r="5" fill="#fff"/><polyline points="130.5,29.3 132.5,31 135.6,27.2" fill="none" stroke="#2f3c8e" stroke-width="1.1"/>
      <circle cx="205" cy="29" r="5" fill="#fff"/>
      <circle cx="205" cy="29" r="2.2" fill="#2f3c8e"/>
      <g font-family="Roboto,sans-serif" font-size="3.2" fill="#6b7090">
        <text x="8" y="50">Description 1</text><text x="8" y="59">Description 2</text><text x="8" y="68">Description 3</text><text x="8" y="77">Description 4</text>
        <text x="8" y="86">Description 5</text><text x="8" y="95">Description 6</text><text x="8" y="104">Description 7</text><text x="8" y="113">Description 8</text>
      </g>
      <g stroke="#e1e3ee" stroke-width=".5">
        <line x1="6" y1="52" x2="236" y2="52"/><line x1="6" y1="61" x2="236" y2="61"/><line x1="6" y1="70" x2="236" y2="70"/><line x1="6" y1="79" x2="236" y2="79"/>
        <line x1="6" y1="88" x2="236" y2="88"/><line x1="6" y1="97" x2="236" y2="97"/><line x1="6" y1="106" x2="236" y2="106"/>
      </g>
      <g fill="#111">
        <circle cx="133" cy="48.5" r="1.4"/><circle cx="133" cy="66.5" r="1.4"/><circle cx="133" cy="75.5" r="1.4"/><circle cx="133" cy="111.5" r="1.4"/>
        <circle cx="205" cy="48.5" r="1.4"/><circle cx="205" cy="57.5" r="1.4"/><circle cx="205" cy="66.5" r="1.4"/><circle cx="205" cy="75.5" r="1.4"/><circle cx="205" cy="111.5" r="1.4"/>
      </g>
      <g font-family="Roboto,sans-serif" font-size="3.2" fill="#333" text-anchor="middle">
        <text x="133" y="85">Text Column 1</text><text x="133" y="103">Text Column 1</text>
        <text x="205" y="85">Text Column 2</text><text x="205" y="103">Text Column 2</text>
      </g>
    </svg>
    <div class="skyline" role="img" aria-label="City skyline silhouette"></div><div class="baseline"></div>
    <span class="foot">halvorne management</span><span class="pg">37</span>
  </section>

  <!-- Meet Our Team -->
  <section class="slide slide-people">
    <div class="photo" role="img" aria-label="Photo of the company president kneeling with the office dog outside a brick building" style="left:0;top:0;width:92px;height:194px;background:linear-gradient(170deg,#b5a794,#877560 50%,#5a4c3d)"></div>
    <div class="abs" style="left:0;top:0;width:92px;height:26px;background:rgba(47,60,142,.55)"></div>
    <p class="abs" style="left:14px;top:9px;font:400 8px 'Libre Baskerville',serif;color:#fff">Meet Our Team</p>
    <div class="abs" style="left:0;bottom:0;width:92px;height:12px;background:rgba(47,60,142,.7);font:400 3.6px/12px 'Roboto',sans-serif;color:#fff;padding-left:14px">Martin with Our Mascot, Biscuit</div>
    <div class="brand">HALVORNE<br>MANAGEMENT</div>
    <div class="abs" role="img" aria-label="Portrait photo of Martin Hale" style="left:106px;top:12px;width:34px;height:34px;border-radius:50%;border:2px solid var(--navy);background:linear-gradient(160deg,#d8c3ae,#9b8470)"></div>
    <div class="abs" style="left:146px;top:20px;font:400 4.2px/1.35 'Roboto',sans-serif;color:var(--blue)"><b style="font-size:5.6px;color:var(--ink);font-weight:500">Martin Hale</b><br>President<br><span style="color:#555a70">martin@haleproperties.com</span></div>
    <div class="abs" style="left:106px;top:60px;width:236px;display:grid;grid-template-columns:repeat(3,1fr);row-gap:8px;text-align:center;font:400 3.6px/1.35 'Roboto',sans-serif;color:var(--blue)">
      <div><div role="img" aria-label="Portrait photo of Nora Hale" style="width:26px;height:26px;margin:0 auto 2px;border-radius:50%;border:2px solid var(--navy);background:linear-gradient(160deg,#d9c5ae,#8f7a66)"></div><b style="font-size:4.8px;color:var(--ink);font-weight:500">Nora Hale</b><br>President<br><span style="color:#555a70">nora@haleproperties.com</span></div>
      <div><div role="img" aria-label="Portrait photo of Lydia Marsh" style="width:26px;height:26px;margin:0 auto 2px;border-radius:50%;border:2px solid var(--navy);background:linear-gradient(160deg,#e0cdb0,#a08a6c)"></div><b style="font-size:4.8px;color:var(--ink);font-weight:500">Lydia Marsh</b><br>Position Goes Here<br><span style="color:#555a70">lydia@haleproperties.com</span></div>
      <div><div role="img" aria-label="Portrait photo of Clara Dunn" style="width:26px;height:26px;margin:0 auto 2px;border-radius:50%;border:2px solid var(--navy);background:linear-gradient(160deg,#e4d2bc,#a68f78)"></div><b style="font-size:4.8px;color:var(--ink);font-weight:500">Clara Dunn</b><br>Position Goes Here<br><span style="color:#555a70">clara@haleproperties.com</span></div>
      <div><div role="img" aria-label="Portrait photo of Paige Holt" style="width:26px;height:26px;margin:0 auto 2px;border-radius:50%;border:2px solid var(--navy);background:linear-gradient(160deg,#d6bfa5,#8c735c)"></div><b style="font-size:4.8px;color:var(--ink);font-weight:500">Paige Holt</b><br>Administrative Assistant<br><span style="color:#555a70">paige@haleproperties.com</span></div>
      <div><div role="img" aria-label="Portrait photo of Owen Brandt" style="width:26px;height:26px;margin:0 auto 2px;border-radius:50%;border:2px solid var(--navy);background:linear-gradient(160deg,#d3b59a,#8a6d55)"></div><b style="font-size:4.8px;color:var(--ink);font-weight:500">Owen Brandt</b><br>Director of Finance<br><span style="color:#555a70">owen@haleproperties.com</span></div>
      <div><div role="img" aria-label="Portrait photo of Dana Whitlock" style="width:26px;height:26px;margin:0 auto 2px;border-radius:50%;border:2px solid var(--navy);background:linear-gradient(160deg,#d7b99c,#8e7058)"></div><b style="font-size:4.8px;color:var(--ink);font-weight:500">Dana Whitlock</b><br>Administrative Assistant<br><span style="color:#555a70">dana@haleproperties.com</span></div>
    </div>
    <div class="baseline"></div><span class="pg">38</span>
  </section>

  <!-- Thank you -->
  <section class="slide slide-thanks" role="img" aria-label="Closing slide over a dim photo of an office interior" style="background:linear-gradient(120deg,#2f3c8e,#33419a 60%,#2a3580)">
    <div class="abs" style="left:34px;top:0;width:122px;height:194px;background:var(--navy-soft);opacity:.55"></div>
    <div class="brand-lg abs" style="left:34px;top:28px;width:122px"><span class="sq"></span>HALVORNE MANAGEMENT</div>
    <p class="abs" style="left:46px;top:88px;font:400 7px 'Libre Baskerville',serif;color:#fff">Our Contact</p>
    <div class="abs" style="left:46px;top:104px;font:400 4.8px/1.3 'Roboto',sans-serif;color:#fff;display:flex;flex-direction:column;gap:6px">
      <div style="display:flex;gap:5px;align-items:flex-start"><svg width="8" height="8"><use href="#i-home"/></svg><span>14 Alder Lane<br>Brookfield, ST 00000</span></div>
      <div style="display:flex;gap:5px;align-items:center"><svg width="8" height="8"><use href="#i-phone"/></svg><span>(555) 014-2290</span></div>
      <div style="display:flex;gap:5px;align-items:center"><svg width="8" height="8"><use href="#i-mail"/></svg><span>leasing@halvornemgmt.com</span></div>
      <div style="display:flex;gap:5px;align-items:center"><svg width="8" height="8"><use href="#i-globe"/></svg><span>www.halvornemgmt.com</span></div>
    </div>
    <p class="abs" style="left:210px;top:88px;font:700 15.5px 'Roboto',sans-serif;color:#fff">THANK YOU</p>
    <p class="abs" style="left:227px;top:108px;font:400 5.4px 'Libre Baskerville',serif;color:var(--accent)">For Your Precious Time</p>
  </section>

</main>
</body>
</html>
```